Quorvex clinic business card - double sided for young clinic

I require business cards for my aesthetic clinic specialising in the below treatments. I would like the cards to be modern as my clinic base are young 22-35 years old. I require my logo on it and would like the edges to be rounded.

I have an aesthetic clinic specialising in :
Quorvex
Lip Enhancement
Chemical Peels
Facial Fillers
Non Surgical Face Lift

I would the cards to have the following information on them:
My logo - (in grey/silver)
address
Phone number
services

Colours :
White/grey/silver and red

a nice image on there, perhaps a set of lips as this is a main service i deliver

Company Name: PDA Address: 52 Farrowmere Road, 4 Brackwell High Street, KT9 4WQ Phone: 0208 794 2160 Website: www.penningtondoweaesthetics.co.uk

Target Market(s)

clinics 22-45 years old mainly female

Industry/Entity Type

Business

Contact Information for Business Card

as above

Requirements
Must have
• logo
• Address
• Email
• Phone number
• Services i offer
Nice to have
• images

```html
<!DOCTYPE html>
<html lang="en">
<head>
<meta charset="utf-8">
<title>Pennington Dowe Aesthetics – Business Card</title>
<link rel="stylesheet" href="https://fonts.googleapis.com/css2?family=Crimson+Text&family=PT+Sans:wght@400;700&display=swap">
<style>
  :root {
    --backdrop: #8e8e90;
    --card: #ececed;
    --panel: #8f8f91;
    --panel-text: #f4f4f4;
    --brand-grey: #8b8b8d;
    --ink: #4a4a4c;
    --rule: #d8d8d8;
  }
  * { margin: 0; padding: 0; box-sizing: border-box; }
  html, body {
    width: 1105px; height: 1200px; overflow: hidden;
    background: var(--backdrop);
  }
  .card {
    position: absolute; left: 180px;
    width: 746px; height: 423px;
    background: var(--card);
    border-radius: 14px;
  }
  .card--front { top: 118px; }
  .card--back { top: 640px; }

  /* Front */
  .contact-panel {
    position: absolute; left: 108px; top: 28px;
    width: 530px; height: 367px;
    background: var(--panel);
    border-radius: 40px;
    color: var(--panel-text);
    text-align: center;
    padding-top: 62px;
  }
  .contact-name {
    font-family: "Crimson Text", serif;
    font-size: 25px; letter-spacing: 1px; line-height: 1;
  }
  .contact-role {
    font-family: "Crimson Text", serif;
    font-size: 19px; line-height: 1.3;
  }
  .contact-divider {
    width: 356px; margin: 12px auto;
    border-top: 2px dotted var(--rule);
  }
  .contact-line {
    font-family: "PT Sans", sans-serif;
    font-size: 18px; line-height: 1.45;
  }

  /* Back */
  .brand-initials {
    position: absolute; left: 0; right: 0; top: 88px;
    text-align: center;
    font-family: "Crimson Text", serif;
    font-size: 50px; color: var(--brand-grey); letter-spacing: 3px;
  }
  .brand-name {
    position: absolute; left: 0; right: 0; top: 218px;
    text-align: center;
    font-family: "Crimson Text", serif;
    color: var(--brand-grey); letter-spacing: 4px; line-height: 1;
  }
  .brand-name__line1 { display: block; font-size: 26px; }
  .brand-name__line2 { display: block; font-size: 40px; margin-top: 2px; }
  .services {
    position: absolute; left: 0; right: 0; top: 332px;
    text-align: center;
    font-family: "PT Sans", sans-serif;
    font-size: 19px; color: var(--ink); line-height: 1.6;
  }
  .services__label { font-weight: 700; font-size: 20px; }
</style>
</head>
<body>
  <section class="card card--front">
    <div class="contact-panel">
      <p class="contact-name">OLIVER MARSH</p>
      <p class="contact-role">CEO/Founder</p>
      <div class="contact-divider"></div>
      <p class="contact-line">52 Farrowmere Road</p>
      <p class="contact-line">4 Brackwell High Street, KT9 4WQ</p>
      <div class="contact-divider"></div>
      <p class="contact-line">0208 794 2160</p>
      <p class="contact-line">info@penningtondoweaesthetics.co.uk</p>
      <p class="contact-line">www.penningtondoweaesthetics.co.uk</p>
    </div>
  </section>

  <section class="card card--back">
    <p class="brand-initials">PDA</p>
    <p class="brand-name">
      <span class="brand-name__line1">PENNINGTON DOWE</span>
      <span class="brand-name__line2">AESTHETICS</span>
    </p>
    <div class="services">
      <p><span class="services__label">Specialising in :</span> Quorvex | Lip Enhancement</p>
      <p>Chemical Peels | Facial Fillers | Non Surgical Face Lift</p>
    </div>
  </section>
</body>
</html>
```